Norvane Builders Business Card

Modern and Professional Business Card for a Med size construction/development company.

See the samples below for the design I like … but I need ideas for incorporating the red company logo while still keeping the clean look of the card samples that are attached.

Logo and tag line on the back … info on the front.

Tagline: Solid Work from the Footing Up

Target Market(s)

Med-Large General Contractors

Contact Information for Business Card

Norvane Builders Limited
42 Brenton Street
Elk Harbour, NL
B3K 7T2

t: 709-555-0147
f: 709-555-0192
w: www.norvanebuilders-example.com

Font styles to use
Sans Serif

Colors
fbee3e

Requirements
Must have
• I like the black and yellow designs of the attached samples …. but I'm not sure how to incorporate the red Norvane Builders logo into that design??
Nice to have
• Construction safety strips

```html
<!DOCTYPE html>
<html lang="en">
<head>
<meta charset="utf-8">
<title>Norvane Builders Limited — Business Card</title>
<link rel="stylesheet" href="https://fonts.googleapis.com/css2?family=Oswald:wght@500;700&family=Cinzel:wght@600&display=swap">
<style>
  :root {
    --page: #ffffff;
    --ink: #111111;
    --carbon-dark: #060708;
    --carbon-light: #2a2c2f;
    --safety-yellow: #fbee3e;
    --band-yellow: #ffdf14;
    --olive: #4a4a22;
    --tagline: #f2ec8a;
    --logo-text: #ffffff;
  }
  * { margin: 0; padding: 0; box-sizing: border-box; }
  html, body { width: 1200px; height: 1196px; overflow: hidden; background: var(--page); }
  .canvas { position: relative; width: 1200px; height: 1196px; }

  .card {
    position: absolute; left: 214px; width: 771px; height: 471px; overflow: hidden;
    box-shadow: 14px 16px 18px rgba(0,0,0,0.35);
    background: linear-gradient(135deg, var(--carbon-light) 0%, var(--carbon-dark) 45%, #111 75%, var(--carbon-light) 100%);
  }
  .card--back { top: 59px; }
  .card--front { top: 591px; }
  .carbon-texture { position: absolute; inset: 0; }

  .wordmark {
    position: absolute; text-align: center; color: var(--logo-text);
    font-family: "Oswald", sans-serif; font-weight: 500; text-transform: uppercase; line-height: 1;
  }
  .wordmark__mark { display: inline-block; background: var(--safety-yellow); vertical-align: middle; }
  .card--back .wordmark { left: 140px; top: 90px; width: 510px; }
  .card--back .wordmark__name { font-size: 80px; letter-spacing: 2px; }
  .card--back .wordmark__sub { font-size: 40px; letter-spacing: 4px; margin-top: 18px; }
  .card--back .wordmark__mark { width: 18px; height: 18px; margin-right: 12px; }

  .tagline-band { position: absolute; left: 0; top: 316px; width: 771px; height: 66px; }
  .tagline {
    position: absolute; left: 0; width: 771px; top: 327px; text-align: center;
    font-family: "Cinzel", serif; font-weight: 600; font-size: 34px; letter-spacing: -0.5px;
    color: var(--tagline); font-variant: small-caps; white-space: nowrap;
  }

  .front-art { position: absolute; inset: 0; }
  .contact { position: absolute; left: 126px; font-family: "Oswald", sans-serif; font-weight: 700; color: var(--ink); line-height: 1.2; }
  .contact--phone { top: 113px; font-size: 26px; line-height: 1.25; letter-spacing: -0.5px; }
  .contact--address { top: 206px; font-size: 18px; line-height: 1.42; letter-spacing: -0.4px; }
  .contact--web { top: 318px; font-size: 17px; letter-spacing: -0.4px; }

  .card--front .wordmark { left: 420px; top: 166px; width: 330px; }
  .card--front .wordmark__name { font-size: 62px; letter-spacing: 1px; }
  .card--front .wordmark__sub { font-size: 28px; letter-spacing: 3px; margin-top: 14px; }
  .card--front .wordmark__mark { width: 13px; height: 13px; margin-right: 8px; }

  .caption {
    position: absolute; left: 0; width: 1200px; top: 1126px; text-align: center;
    font-family: "Oswald", sans-serif; font-weight: 700; font-size: 25px; color: var(--ink); letter-spacing: -0.3px;
  }
</style>
</head>
<body>
<main class="canvas">

  <section class="card card--back" aria-label="Card back with name and tagline">
    <div class="carbon-texture" role="img" aria-label="Dark carbon fibre texture background"></div>
    <div class="wordmark">
      <div class="wordmark__name"><span class="wordmark__mark"></span>Norvane</div>
      <div class="wordmark__sub">Builders Limited</div>
    </div>
    <svg class="tagline-band" viewBox="0 0 771 66" aria-hidden="true">
      <g fill="var(--olive)" opacity="0.85">
        <polygon points="40,0 98,0 78,66 20,66"/>
        <polygon points="102,0 158,0 138,66 82,66"/>
        <polygon points="162,0 218,0 198,66 142,66"/>
        <polygon points="222,0 278,0 258,66 202,66"/>
        <polygon points="282,0 338,0 318,66 262,66"/>
        <polygon points="342,0 398,0 378,66 322,66"/>
        <polygon points="402,0 458,0 438,66 382,66"/>
        <polygon points="462,0 518,0 498,66 442,66"/>
        <polygon points="522,0 578,0 558,66 502,66"/>
        <polygon points="582,0 638,0 618,66 562,66"/>
        <polygon points="642,0 698,0 678,66 622,66"/>
        <polygon points="702,0 752,0 732,66 682,66"/>
      </g>
    </svg>
    <p class="tagline">Solid Work from the Footing Up</p>
  </section>

  <section class="card card--front" aria-label="Card front with contact details">
    <div class="carbon-texture" role="img" aria-label="Dark carbon fibre texture background"></div>
    <svg class="front-art" viewBox="0 0 771 471" aria-hidden="true">
      <polygon points="0,0 272,0 401,471 0,471" fill="var(--band-yellow)"/>
      <polygon points="272,0 303,0 430,471 401,471" fill="var(--safety-yellow)"/>
      <polygon points="303,0 340,0 468,471 430,471" fill="var(--olive)"/>
      <g stroke="#222" stroke-width="4" opacity="0.7">
        <line x1="310" y1="40" x2="348" y2="42"/>
        <line x1="330" y1="100" x2="366" y2="102"/>
        <line x1="345" y1="160" x2="382" y2="162"/>
        <line x1="362" y1="220" x2="399" y2="222"/>
        <line x1="378" y1="280" x2="416" y2="282"/>
        <line x1="394" y1="340" x2="432" y2="342"/>
        <line x1="410" y1="400" x2="448" y2="402"/>
      </g>
      <polygon points="54,25 282,25 401,471 54,471" fill="#ffffff"/>
      <g fill="var(--band-yellow)">
        <rect x="52" y="137" width="30" height="20"/>
        <circle cx="90" cy="147" r="25"/>
        <rect x="52" y="231" width="30" height="20"/>
        <circle cx="90" cy="241" r="25"/>
        <rect x="52" y="321" width="30" height="20"/>
        <circle cx="88" cy="331" r="25"/>
      </g>
      <g fill="none" stroke="#fff" stroke-width="2.4" stroke-linecap="round" stroke-linejoin="round">
        <path d="M80,138 l5,-3 4,8 -3,3 c2,5 5,8 10,10 l3,-3 8,4 -3,5 c-14,0 -25,-11 -24,-24z"/>
        <path d="M96,134 a8,8 0 0 1 8,8 M96,129 a13,13 0 0 1 13,13"/>
        <path d="M90,255 c-8,-10 -11,-14 -11,-19 a11,11 0 0 1 22,0 c0,5 -3,9 -11,19z"/>
        <circle cx="90" cy="236" r="3.5"/>
        <circle cx="88" cy="331" r="14"/>
        <ellipse cx="88" cy="331" rx="6" ry="14"/>
        <line x1="74" y1="331" x2="102" y2="331"/>
        <path d="M77,323 h22 M77,339 h22"/>
      </g>
    </svg>
    <p class="contact contact--phone">709-555-0147<br>709-555-0192</p>
    <p class="contact contact--address">42 Brenton Street<br>Elk Harbour, NL<br>B3K 7T2</p>
    <p class="contact contact--web">www.norvanebuilders-example.com</p>
    <div class="wordmark">
      <div class="wordmark__name"><span class="wordmark__mark"></span>Norvane</div>
      <div class="wordmark__sub">Builders Limited</div>
    </div>
  </section>

  <p class="caption">Business Card for “Norvane Builders Limited”</p>
</main>
</body>
</html>
```